Bottle label design for a mulberry brandy

Please create a label design for a mulberry brandy. The registered brand name is "Tavrik"
The brandy will be produced in Armenia from 100% mulberry.
Color of the product: transparent.
The product will be sold worldwide. The price will be between 30 and 50 USD. So the product will be in premium category.
Therefore we need a solid design, appropriate to the product price category. The design, however, needs to be modern and optimistic.
You can have mulberries on the label or not have, it is up to you.
We have chosen for the product some bottle types, the links to the available bottles you can find in the attachment. Ideally you show a picture of your label on the bottle you selected.

worldwide

```html
<!DOCTYPE html>
<html lang="en">
<head>
<meta charset="utf-8">
<title>Tavrik Mulberry Brandy – Label</title>
<link rel="stylesheet" href="https://fonts.googleapis.com/css2?family=Roboto+Slab:wght@400&family=Varela+Round&family=Tinos&display=swap">
<style>
  :root {
    --paper: #ffffff;
    --ink: #2b2b2b;
    --ink-soft: #444444;
    --rule: #555555;
    --art-light: #d6d6d6;
    --art-dark: #9a9a9a;
  }
  html, body {
    margin: 0;
    padding: 0;
    width: 879px;
    height: 1200px;
    overflow: hidden;
    background: var(--paper);
  }
  .label {
    position: relative;
    width: 879px;
    height: 1200px;
    background: var(--paper);
    color: var(--ink);
  }
  .label__illustration {
    position: absolute;
    left: 300px;
    top: 180px;
    width: 279px;
    height: 380px;
    border-radius: 6px;
    background: linear-gradient(180deg, var(--art-light), var(--art-dark));
  }
  .label__text {
    position: absolute;
    left: 0;
    width: 100%;
    margin: 0;
    text-align: center;
    line-height: 1;
    white-space: nowrap;
  }
  .label__brand {
    top: 592px;
    font-family: "Roboto Slab", serif;
    font-weight: 400;
    font-size: 136px;
    letter-spacing: 2px;
  }
  .label__product {
    top: 745px;
    font-family: "Varela Round", sans-serif;
    font-size: 66px;
    color: var(--ink-soft);
  }
  .label__divider {
    position: absolute;
    left: 244px;
    top: 835px;
    width: 391px;
    height: 10px;
  }
  .label__content {
    top: 870px;
    font-family: "Tinos", serif;
    font-size: 44px;
  }
  .label__origin {
    top: 965px;
    font-family: "Tinos", serif;
    font-size: 34px;
  }
</style>
</head>
<body>
  <main class="label">
    <div class="label__illustration" role="img" aria-label="Engraved illustration of a mulberry hanging from a twig"></div>
    <h1 class="label__text label__brand">Tavrik</h1>
    <p class="label__text label__product">mulberry brandy</p>
    <svg class="label__divider" viewBox="0 0 391 10" aria-hidden="true">
      <line x1="3" y1="5" x2="388" y2="5" stroke="#555555" stroke-width="2"/>
      <circle cx="3" cy="5" r="3" fill="#555555"/>
      <circle cx="388" cy="5" r="3" fill="#555555"/>
    </svg>
    <p class="label__text label__content">100% mulberry</p>
    <p class="label__text label__origin">Made in Armenia</p>
  </main>
</body>
</html>
```